Business Card for a Dental Office

The design should communicate integrity, quality and reliability. We also want the card look elegant, simple, but still stand out, different from the traditional-dental-office business card.

Industry/Entity Type

Business

```html
<!DOCTYPE html>
<html lang="en">
<head>
<meta charset="utf-8">
<title>Northfield Dental Centre – Business Card</title>
<link href="https://fonts.googleapis.com/css2?family=Open+Sans:wght@400;600;700&display=swap" rel="stylesheet">
<style>
  :root {
    --page: #e8e5e1;
    --card: #ffffff;
    --ink: #111111;
    --gold: #c9a515;
    --gold-bright: #f2e21c;
    --gold-deep: #8a6d12;
    --rule: #222222;
  }
  * { margin: 0; padding: 0; box-sizing: border-box; }
  html, body {
    width: 1200px; height: 1000px; overflow: hidden;
    background: var(--page);
    font-family: "Open Sans", Arial, sans-serif;
    color: var(--ink);
  }
  .card {
    position: absolute; left: 265px; width: 665px; height: 397px;
    background: var(--card);
    box-shadow: 0 4px 14px rgba(0,0,0,0.18);
    overflow: hidden;
  }
  .card--front { top: 73px; }
  .card--back { top: 533px; }

  .brand { position: absolute; display: flex; align-items: center; gap: 14px; white-space: nowrap; }
  .brand__square { width: 46px; height: 46px; background: var(--ink); flex: none; }
  .brand__name {
    font-weight: 700; font-size: 24px; line-height: 1; letter-spacing: 0.3px;
    text-transform: uppercase; color: var(--ink);
  }
  .card--front .brand { left: 115px; top: 90px; }
  .card--back .brand { left: 97px; top: 159px; }
  .card--back .brand__name { font-size: 26px; }

  .contact {
    position: absolute; right: 352px; top: 208px;
    text-align: right; font-size: 15px; line-height: 21.5px;
  }
  .contact__address { margin-bottom: 2px; }
  .contact__line { display: flex; justify-content: flex-end; align-items: center; gap: 6px; }
  .contact__icon { width: 16px; height: 12px; flex: none; }

  .divider {
    position: absolute; left: 332px; top: 212px; width: 2px; height: 120px;
    background: var(--rule);
  }

  .doctors { position: absolute; left: 352px; top: 210px; list-style: none; }
  .doctors li { font-size: 17px; font-weight: 700; line-height: 34px; }
  .doctors .degree { font-weight: 400; font-size: 15px; }

  .band {
    position: absolute; left: 0; bottom: 0; width: 100%; height: 32px;
    background: linear-gradient(90deg, #000 0%, #000 46%, var(--gold-deep) 52%, var(--gold-bright) 85%, #d9c400 100%);
  }
</style>
</head>
<body>

<section class="card card--front">
  <div class="brand">
    <span class="brand__square"></span>
    <span class="brand__name">Northfield Dental Centre</span>
  </div>

  <div class="contact">
    <p class="contact__address">418 Harbour Street, Westfield,<br>MB R3B 2K7</p>
    <p class="contact__line">Toll Free 1 (888) 555 0142</p>
    <p class="contact__line">1 (204) 555 0187
      <svg class="contact__icon" viewBox="0 0 16 12" aria-hidden="true"><path fill="#c9a515" d="M1 4c2-3 12-3 14 0l-1 2-3-1V3H5v2L2 6zM4 7h8l2 4H2z"/></svg>
    </p>
    <p class="contact__line">1 (204) 555 0163
      <svg class="contact__icon" viewBox="0 0 16 12" aria-hidden="true"><path fill="#c9a515" d="M4 0h8v3H4zM1 4h14v5h-3V7H4v2H1zM4 8h8v4H4z"/></svg>
    </p>
    <p class="contact__line">hello@northfielddental.net
      <svg class="contact__icon" viewBox="0 0 16 12" aria-hidden="true"><path fill="#c9a515" d="M0 0h16v12H0z"/><path fill="none" stroke="#fff" stroke-width="1.2" d="M0.5 0.5 8 7l7.5-6.5"/></svg>
    </p>
  </div>

  <div class="divider"></div>

  <ul class="doctors">
    <li>Dr. Martin G. Halvorsen, <span class="degree">DMD</span></li>
    <li>Dr. Peter A. Lindqvist, <span class="degree">DMD</span></li>
    <li>Dr. Clara A. Moreno, <span class="degree">DMD</span></li>
    <li>Dr. Anh T. Nguyen, <span class="degree">DDS</span></li>
  </ul>

  <div class="band"></div>
</section>

<section class="card card--back">
  <div class="brand">
    <span class="brand__square"></span>
    <span class="brand__name">Northfield Dental Centre</span>
  </div>
</section>

</body>
</html>
```